Corvina Baste College of Nursing website

Nursing college needs a fresh, streamlined website. Many of the items on our website are required by accreditation organizations.

```html
<!DOCTYPE html>
<html lang="en">
<head>
<meta charset="utf-8">
<title>Corvina Baste College of Nursing</title>
<link href="https://fonts.googleapis.com/css2?family=Outfit:wght@300;400;500;600;700&display=swap" rel="stylesheet">
<style>
:root{
  --green:#0e7a4e;
  --purple:#6a1b7f;
  --purple-dark:#5a1470;
  --ink:#1f1f24;
  --muted:#6b6b74;
  --lav:#f3eef6;
  --dark:#1b1d22;
  --white:#fff;
}
*{box-sizing:border-box;margin:0;padding:0}
html,body{width:1200px;height:3381px;overflow:hidden}
body{font-family:"Outfit",sans-serif;color:var(--ink);background:#fff;position:relative}
.abs{position:absolute}
.btn{position:absolute;background:var(--purple);color:#fff;border-radius:24px;font-weight:600;font-size:15px;display:flex;align-items:center;justify-content:center}
/* header */
.topline{left:0;top:0;width:1200px;height:3px;background:#123a4a}
.brand{left:111px;top:20px;display:flex;align-items:center;gap:12px}
.brand-dot{width:58px;height:58px;border-radius:50%;background:var(--purple)}
.brand-name{font-size:24px;font-weight:500;line-height:1.15;color:#3a3a44}
.contact{display:flex;align-items:center;gap:22px;top:30px}
.contact .ic{width:60px;height:60px;border-radius:50%;background:var(--green);display:flex;align-items:center;justify-content:center}
.contact small{display:block;font-size:13px;color:#333}
.contact b{font-size:20px;font-weight:600;color:#222}
.nav{left:0;top:122px;width:1200px;height:58px;background:var(--purple);display:flex;align-items:center}
.nav .home{width:195px;height:58px;background:var(--green)}
.nav a{position:absolute;top:21px;color:#fff;font-size:13px;font-weight:600;text-decoration:none}
/* hero */
.hero{left:0;top:180px;width:1200px;height:427px;background:linear-gradient(135deg,#0d2435 0%,#1f5c78 45%,#c7d6de 62%,#244e66 80%,#0f2533 100%)}
.hero h1{position:absolute;top:100px;width:1200px;text-align:center;color:#fff;font-size:58px;font-weight:600}
.hero p{position:absolute;top:185px;left:250px;width:700px;text-align:center;color:#fff;font-size:20px;line-height:35px}
.hero-notch{left:570px;top:584px;width:60px;height:30px;background:#fff;border-radius:30px 30px 0 0}
/* mission */
.photo{position:absolute}
.mission h2{position:absolute;left:675px;top:678px;font-size:40px;font-weight:500}
.mtext{position:absolute;left:677px;width:420px;font-size:14px;line-height:29px;color:var(--muted)}
.goal{position:absolute;left:695px;display:flex;align-items:center;gap:12px;font-size:14px;color:var(--muted)}
.goal i{width:24px;height:24px;border-radius:50%;background:#e3f1ea;display:flex;align-items:center;justify-content:center}
/* academics */
.acad{left:0;top:1235px;width:1200px;height:596px;background:var(--lav)}
.acad h2{position:absolute;left:110px;top:62px;font-size:40px;font-weight:500}
.card{position:absolute;top:145px;width:316px;height:385px;background:#fff}
.card .img{height:218px}
.card .tag{position:absolute;left:26px;top:202px;height:32px;padding:0 24px;border-radius:16px;background:var(--green);color:#fff;font-size:13px;font-weight:500;display:flex;align-items:center}
.card h3{position:absolute;left:24px;top:252px;font-size:22px;font-weight:500}
.card p{position:absolute;left:24px;top:290px;width:272px;font-size:13px;line-height:23px;color:var(--muted)}
/* why */
.why{left:0;top:1831px;width:1200px;height:441px;background:linear-gradient(90deg,#2c2f33,#46484a 40%,#3b3d40 70%,#26282b)}
.why h2{position:absolute;top:70px;width:1200px;text-align:center;color:#fff;font-size:42px;font-weight:500}
.why p{position:absolute;top:140px;left:250px;width:700px;text-align:center;color:#fff;font-size:15px;line-height:29px}
.why .phone{position:absolute;left:977px;top:0;font-size:24px;font-weight:600;color:rgba(255,255,255,.25)}
.feat{position:absolute;top:238px;width:160px;text-align:center;color:#fff;font-size:15px}
.feat .c{width:88px;height:88px;margin:0 auto 22px;border:1.5px solid #fff;border-radius:50%;display:flex;align-items:center;justify-content:center}
.feat .c.on{background:var(--purple);border-color:var(--purple)}
/* news */
.news h2{position:absolute;left:109px;top:2375px;font-size:41px;font-weight:500}
.ncard{position:absolute;left:109px;top:2465px;width:542px;height:355px;background:#fff;border-left:5px solid var(--green);border-radius:14px;box-shadow:0 10px 40px rgba(0,0,0,.12)}
.ncard h3{position:absolute;left:42px;top:32px;width:420px;font-size:24px;line-height:40px;font-weight:500}
.ncard p{position:absolute;left:42px;top:128px;width:460px;font-size:13px;line-height:29px;color:var(--muted)}
.arr{position:absolute;top:2853px;width:22px;height:22px;border-radius:50%;display:flex;align-items:center;justify-content:center}
/* footer */
.foot{left:0;top:3000px;width:1200px;height:381px;background:var(--dark);color:#fff}
.seal{position:absolute;left:132px;top:70px;width:186px;height:186px;border-radius:50%;background:#fff;border:4px solid #d9d9e6;display:flex;align-items:center;justify-content:center;text-align:center}
.seal span{color:var(--purple);font-size:18px;font-weight:600;line-height:1.3}
.foot h4{position:absolute;top:75px;font-size:20px;font-weight:500}
.flist{position:absolute;top:112px;font-size:15px;line-height:29.5px}
.fbtn{position:absolute;left:534px;top:298px;width:165px;height:54px;border-radius:28px;background:var(--green);color:#fff;font-size:16px;font-weight:600;display:flex;align-items:center;justify-content:center}
.copy{position:absolute;left:110px;top:343px;font-size:12px}
.social{position:absolute;right:110px;top:343px;font-size:11px;word-spacing:4px}
</style>
</head>
<body>
<div class="abs topline"></div>
<header>
  <div class="abs brand"><div class="brand-dot"></div><div class="brand-name">Corvina Baste<br>College of Nursing</div></div>
  <div class="abs contact" style="left:556px">
    <div class="ic"><svg width="20" height="20" viewBox="0 0 24 24" fill="#fff"><path d="M6.6 10.8a15 15 0 0 0 6.6 6.6l2.2-2.2c.3-.3.7-.4 1-.2 1.1.4 2.3.6 3.6.6.6 0 1 .4 1 1V20c0 .6-.4 1-1 1A17 17 0 0 1 3 4c0-.6.4-1 1-1h3.5c.6 0 1 .4 1 1 0 1.3.2 2.5.6 3.6.1.3 0 .7-.2 1z"/></svg></div>
    <div><small>Register</small><b>(555) 304-2190/2191</b></div>
  </div>
  <div class="abs contact" style="left:869px">
    <div class="ic"><svg width="20" height="20" viewBox="0 0 24 24" fill="#fff"><path d="M6.6 10.8a15 15 0 0 0 6.6 6.6l2.2-2.2c.3-.3.7-.4 1-.2 1.1.4 2.3.6 3.6.6.6 0 1 .4 1 1V20c0 .6-.4 1-1 1A17 17 0 0 1 3 4c0-.6.4-1 1-1h3.5c.6 0 1 .4 1 1 0 1.3.2 2.5.6 3.6.1.3 0 .7-.2 1z"/></svg></div>
    <div><small>Admissions</small><b>(555) 304-2200</b></div>
  </div>
  <nav class="abs nav">
    <div class="home"></div>
    <a style="left:118px">HOME</a><a style="left:222px">ABOUT US</a><a style="left:351px">ACADEMICS</a>
    <a style="left:495px">POLICIES &amp; HANDBOOKS</a><a style="left:721px">LIBRARY</a>
    <a style="left:839px">CONTACT US</a><a style="left:988px">DONATE NOW</a>
  </nav>
</header>

<section class="abs hero" role="img" aria-label="Gloved hands of surgeons during a procedure">
  <h1>Corvina Baste College of Nursing</h1>
  <p>Corvina Baste College Of Nursing has been educating nurses for over seventy years. Founded in 1945</p>
  <div class="btn" style="left:529px;top:272px;width:142px;height:42px">Get Started</div>
</section>
<div class="abs hero-notch"></div>

<section class="mission">
  <div class="photo" style="left:111px;top:681px;width:236px;height:219px;background:linear-gradient(160deg,#c9b58c,#2f62b3 60%,#223)" role="img" aria-label="Nursing students walking in scrubs"></div>
  <div class="photo" style="left:111px;top:914px;width:236px;height:209px;background:linear-gradient(160deg,#e8e8ea,#233a66 55%,#d8d8dc)" role="img" aria-label="Nursing students practicing on a training manikin"></div>
  <div class="photo" style="left:362px;top:724px;width:238px;height:217px;background:linear-gradient(160deg,#5a7ad6,#1f2e9e 60%,#121a55)" role="img" aria-label="Graduates in caps and gowns"></div>
  <div class="photo" style="left:362px;top:956px;width:238px;height:181px;background:linear-gradient(160deg,#9cc3e4,#3d7cc2 55%,#e6e6e8)" role="img" aria-label="Students studying an anatomy model with an instructor"></div>
  <h2>Mission &amp; Vision</h2>
  <p class="mtext" style="top:744px">Corvina Baste College of Nursing will be nationally recognized for excellence in nursing education, and noted for its comprehensive, innovative academic programs that are responsive to the healthcare challenges of the future.</p>
  <p class="mtext" style="top:874px">Corvina Baste College of Nursing is an independent single-purpose institution.</p>
  <div class="goal" style="top:953px"><i><svg width="12" height="12" viewBox="0 0 12 12"><path d="M2 6l3 3 5-6" stroke="#0e7a4e" stroke-width="2" fill="none"/></svg></i>Goal I: &nbsp; Professional Learning</div>
  <div class="goal" style="top:994px"><i><svg width="12" height="12" viewBox="0 0 12 12"><path d="M2 6l3 3 5-6" stroke="#0e7a4e" stroke-width="2" fill="none"/></svg></i>Goal II: &nbsp;Professional Advancement</div>
  <div class="goal" style="top:1034px"><i><svg width="12" height="12" viewBox="0 0 12 12"><path d="M2 6l3 3 5-6" stroke="#0e7a4e" stroke-width="2" fill="none"/></svg></i>Goal III: &nbsp;Professional Environment</div>
  <div class="btn" style="left:677px;top:1091px;width:125px;height:42px">Read More</div>
</section>

<section class="abs acad">
  <h2>Our Academics</h2>
  <div class="btn" style="left:920px;top:66px;width:169px;height:42px">View All Courses</div>
  <div class="card" style="left:111px">
    <div class="img" style="background:linear-gradient(160deg,#e9ecef,#9aa4b0 60%,#3a3f48)" role="img" aria-label="Students in a video lecture"></div>
    <div class="tag">Coursewell Community</div>
    <h3>Distance Learning</h3>
    <p>CBCN contracted Learnbridge, the company behind Coursewell, to provide Tier 1 support for all CBCN faculty, staff, and students.</p>
  </div>
  <div class="card" style="left:442px">
    <div class="img" style="background:linear-gradient(160deg,#d5d9de,#7d8da0 55%,#3b4a62)" role="img" aria-label="Instructor presenting to a class"></div>
    <div class="tag">EntryPrep Mobile app</div>
    <h3>Entrance Exams</h3>
    <p>Corvina Baste College of Nursing now accepts entrance exams from Testwise, Nursmark or Clinova. Please contact the test administrator</p>
  </div>
  <div class="card" style="left:773px">
    <div class="img" style="background:linear-gradient(160deg,#e6dcd0,#8a3048 55%,#4b5c8a)" role="img" aria-label="Caregiver assisting a patient"></div>
    <div class="tag">Non-Discrimination Policy</div>
    <h3>Disability Services</h3>
    <p>Corvina Baste College of Nursing complies with Section 504 of the Rehabilitation Act Of 1973 and the Americans</p>
  </div>
</section>

<section class="abs why" role="img" aria-label="Students and instructor in a laboratory">
  <div class="phone">555-304-2200</div>
  <h2>Why Choose Us</h2>
  <p>CBCN is an independent single-purpose institution. Its mission is to provide a dynamic career-ladder approach to nursing education to improve professional practice</p>
  <div class="feat" style="left:241px"><div class="c"><svg width="34" height="34" viewBox="0 0 24 24" fill="none" stroke="#fff" stroke-width="2.2"><circle cx="10" cy="10" r="6"/><path d="M15 15l5 5"/></svg></div>Apply Now</div>
  <div class="feat" style="left:427px"><div class="c"><svg width="36" height="36" viewBox="0 0 24 24" fill="#fff"><path d="M12 4L1 9l11 5 9-4v6h2V9z"/><path d="M6 13v4c2 2 10 2 12 0v-4l-6 3z"/></svg></div>Our Successes</div>
  <div class="feat" style="left:612px"><div class="c on"><svg width="34" height="34" viewBox="0 0 24 24" fill="#fff"><circle cx="12" cy="12" r="9" fill="none" stroke="#fff" stroke-width="2"/><circle cx="9" cy="11" r="2.5"/><circle cx="15" cy="11" r="2.5"/><path d="M5 18c1-3 7-3 7 0zM12 18c1-3 7-3 7 0z"/></svg></div>Demographics</div>
  <div class="feat" style="left:798px"><div class="c"><svg width="36" height="36" viewBox="0 0 24 24"><circle cx="12" cy="12" r="10" fill="#fff"/><rect x="10.8" y="10" width="2.4" height="8" fill="#3d3f42"/><circle cx="12" cy="7" r="1.5" fill="#3d3f42"/></svg></div>Information</div>
</section>

<section class="news">
  <h2>News &amp; updates</h2>
  <div class="abs" style="left:557px;top:2353px;width:532px;height:553px;background:linear-gradient(160deg,#c9d4dc,#6b8fb8 50%,#3c74b8 70%,#dfe3e6)" role="img" aria-label="Nursing student in scrubs attending a lecture"></div>
  <div class="ncard">
    <h3>NCAB Pre-accreditation Public Posting Notice</h3>
    <p>The Associate Degree in Nursing Program at Corvina Baste College of Nursing is seeking pre-accreditation status from the National Council for Nursing Accreditation Boards (NCAB). located at 310 Alder Avenue</p>
    <div class="btn" style="left:42px;top:267px;width:123px;height:42px">Read More</div>
  </div>
  <div class="arr" style="left:474px;background:#999"><svg width="12" height="12" viewBox="0 0 12 12"><path d="M10 6H2M5 3L2 6l3 3" stroke="#fff" stroke-width="1.8" fill="none"/></svg></div>
  <div class="arr" style="left:505px;background:#222"><svg width="12" height="12" viewBox="0 0 12 12"><path d="M2 6h8M7 3l3 3-3 3" stroke="#fff" stroke-width="1.8" fill="none"/></svg></div>
</section>

<footer class="abs foot">
  <div class="seal"><span>Corvina Baste<br>College of<br>Nursing</span></div>
  <h4 style="left:409px">QUICK LINKS</h4>
  <div class="flist" style="left:409px">Office Suite<br>Coursewell Lms<br>Student Portal<br>Email<br>Testwise Testing</div>
  <div class="flist" style="left:573px">Proctorly<br>Textline Connect<br>Payroll Hub (Employees Only)<br>Payline Flex (Staff Only)<br>Registry Sonar</div>
  <h4 style="left:825px">CONTACT US</h4>
  <div class="flist" style="left:825px">48 Linden Row, Brookfield,<br>NY 10090<br>(555) 304-2190/2191<br>registrar@corvinabaste.edu (Register)</div>
  <div class="fbtn">Donate Here</div>
  <div class="copy">(C) Copyright 2024 | All Rights Reserved</div>
  <div class="social">Friendspace &nbsp;| &nbsp;Snapgrid &nbsp;| &nbsp;Chirper &nbsp;| &nbsp;Workline</div>
</footer>
</body>
</html>
```